Halvorsen Electric service department flyer

Looking to design a electrical service department flyer. The company has been in San Francisco for 60yrs primarily doing work in the downtown area. https://halvorsenelectric.example/about-halvorsen/
I attached a rough draft of the flyer. I would like to see something with the san francisco downtown skyline watermarked on the front page, open to the second page that describes all services and contact.

```html
<!DOCTYPE html>
<html lang="en">
<head>
<meta charset="utf-8">
<title>Halvorsen Electric – Service Department Flyer</title>
<link rel="stylesheet" href="https://fonts.googleapis.com/css2?family=Poppins:wght@400;500;600;700;800&display=swap">
<style>
  :root{
    --blue:#0b4fae;
    --blue-deep:#083f8f;
    --cyan:#2aa8e2;
    --ink:#1b1b1f;
    --paper:#ffffff;
    --stage:#e3e8ef;
  }
  *{box-sizing:border-box;margin:0;padding:0}
  html,body{width:1200px;height:900px;overflow:hidden}
  body{background:var(--stage);font-family:"Poppins",sans-serif;color:var(--ink);position:relative}
  .page{position:absolute;top:68px;width:540px;height:764px;overflow:hidden;background:var(--blue);box-shadow:0 6px 22px rgba(8,40,90,.18)}
  .page--back{left:40px}
  .page--front{left:620px}
  .page__bg{position:absolute;inset:0}
  .abs{position:absolute}
  .center{left:0;right:0;text-align:center}

  /* Back page */
  .brand{font-weight:800;color:var(--blue);letter-spacing:1.5px;font-size:17px;text-transform:uppercase}
  .brand-mark{display:inline-block;width:10px;height:10px;background:var(--blue);margin-right:7px;vertical-align:1px}
  .why-title{top:98px;font-size:34px;font-weight:800;color:var(--blue);letter-spacing:-.5px}
  .why-rule{top:148px;left:130px;width:280px;height:2px;background:var(--ink)}
  .why-list{top:160px;left:44px;width:460px;display:grid;grid-template-columns:auto auto;justify-content:space-between;gap:4px 16px;list-style:none;font-size:9.5px;font-weight:600;white-space:nowrap}
  .why-list li{display:flex;align-items:center;gap:6px}
  .why-list li::before{content:"";width:7px;height:7px;background:var(--blue-deep);border-radius:1px;flex:none}
  .hours-title{top:204px;font-size:30px;font-weight:800;color:var(--blue)}
  .hours-box{top:252px;left:135px;width:270px;height:62px;border:1.5px solid var(--ink);border-radius:10px;text-align:center;font-size:20px;font-weight:700;line-height:1.15;padding-top:5px}
  .emergency{top:334px;left:120px;display:flex}
  .emergency__tag{background:var(--blue);color:#fff;font-weight:800;font-size:18px;padding:3px 10px}
  .emergency__avail{border:1.5px solid var(--blue);color:var(--blue);font-weight:800;font-size:18px;padding:1px 8px;background:#fff}
  .emergency__phone{top:368px;left:200px;border:1.5px solid var(--blue);font-weight:800;font-size:19px;padding:0 8px;background:#fff}
  .divider{height:3px;background:var(--ink)}
  .estimates-title{top:462px;left:40px;font-size:29px;font-weight:800;color:var(--blue);letter-spacing:-.3px}
  .estimates-sub{top:505px;left:42px;font-size:11.5px;font-weight:500}
  .check-list{list-style:none;font-size:12.5px;font-weight:500}
  .check-list li{display:flex;align-items:center;gap:8px;height:34px}
  .check-list svg{flex:none}
  .contact{top:522px;left:298px;width:242px;height:156px;background:var(--blue);border-radius:12px 0 0 12px;color:#fff;padding:12px 14px}
  .contact__title{font-size:21px;font-weight:700;text-align:center;margin-bottom:6px}
  .contact__row{display:flex;align-items:flex-start;gap:7px;font-size:10.5px;line-height:1.25;margin-bottom:6px}
  .contact__row svg{flex:none;margin-top:1px}

  /* Front page */
  .front-brand{top:266px;font-size:22px;font-weight:800;color:#fff;letter-spacing:3px}
  .front-title{top:336px;font-size:34px;font-weight:700;color:var(--blue);letter-spacing:-.5px}
  .front-intro{top:390px;left:60px;width:420px;text-align:center;font-size:10px;line-height:1.4}
  .front-tagline{top:448px;font-size:17px;font-weight:700;letter-spacing:.3px}
  .front-rule{top:480px;left:28px;width:484px;height:2px;background:var(--ink)}
  .col-title{font-size:15px;font-weight:700;color:var(--blue)}
  .services{top:532px;left:28px;list-style:none;font-size:11px;font-weight:500}
  .services li{display:flex;align-items:center;gap:8px;height:24px;line-height:1.1}
  .services li.is-blue{color:var(--blue)}
  .commercial{top:525px;left:290px;list-style:none;font-size:11px;font-weight:500}
  .commercial li{display:flex;align-items:center;gap:7px;height:22px}
  .photo-thumb{top:640px;width:112px;height:58px;border:3px solid var(--blue);border-radius:10px 0 10px 0;background:linear-gradient(135deg,#4b5d73,#c9a04a 55%,#8797a8)}
</style>
</head>
<body>

<!-- Back page: why choose us, hours, estimates, contact -->
<section class="page page--back" aria-label="Flyer back page">
  <svg class="page__bg" width="540" height="764" viewBox="0 0 540 764" aria-hidden="true">
    <rect width="540" height="764" fill="var(--blue)"/>
    <path d="M0 260 C10 90 140 30 270 30 C400 30 530 90 540 260 L540 705 L0 705 Z" fill="var(--paper)"/>
    <rect y="734" width="540" height="3" fill="#fff"/>
    <rect y="744" width="540" height="2" fill="#fff"/>
  </svg>

  <div class="abs center" style="top:62px"><span class="brand"><span class="brand-mark"></span>Halvorsen Electric</span></div>
  <h2 class="abs center why-title">WHY CHOOSE US</h2>
  <div class="abs why-rule"></div>
  <ul class="abs why-list">
    <li>Customer service is our priority</li>
    <li>Professional, clean and efficient work</li>
    <li>Honest pricing &amp; dependable results</li>
    <li>San Francisco based company since 1966</li>
  </ul>
  <h3 class="abs center hours-title">Hours:</h3>
  <div class="abs hours-box">Mon-Fri:<br>8:00 AM - 5:00 PM</div>
  <div class="abs emergency"><span class="emergency__tag">EMERGENCY</span><span class="emergency__avail">Service Available</span></div>
  <div class="abs emergency__phone">24/7 (415) 555-0142</div>

  <div class="abs divider" style="top:440px;left:40px;width:470px"></div>

  <h2 class="abs estimates-title">Free Estimates Available</h2>
  <p class="abs estimates-sub">Residential • Commercial • 24/7 Emergency Service</p>
  <ul class="abs check-list" style="top:528px;left:42px">
    <li><svg width="16" height="16" viewBox="0 0 16 16"><circle cx="8" cy="8" r="6.8" fill="none" stroke="var(--blue)" stroke-width="1.5"/><path d="M4.8 8.2l2.2 2.2 4.2-4.6" fill="none" stroke="var(--blue)" stroke-width="1.6"/></svg>Electrical Repairs</li>
    <li><svg width="16" height="16" viewBox="0 0 16 16"><circle cx="8" cy="8" r="6.8" fill="none" stroke="var(--blue)" stroke-width="1.5"/><path d="M4.8 8.2l2.2 2.2 4.2-4.6" fill="none" stroke="var(--blue)" stroke-width="1.6"/></svg>Panel Upgrades</li>
    <li><svg width="16" height="16" viewBox="0 0 16 16"><circle cx="8" cy="8" r="6.8" fill="none" stroke="var(--blue)" stroke-width="1.5"/><path d="M4.8 8.2l2.2 2.2 4.2-4.6" fill="none" stroke="var(--blue)" stroke-width="1.6"/></svg>Lighting Installation</li>
    <li><svg width="16" height="16" viewBox="0 0 16 16"><circle cx="8" cy="8" r="6.8" fill="none" stroke="var(--blue)" stroke-width="1.5"/><path d="M4.8 8.2l2.2 2.2 4.2-4.6" fill="none" stroke="var(--blue)" stroke-width="1.6"/></svg>Building maintenance / 24/7 Service</li>
    <li><svg width="16" height="16" viewBox="0 0 16 16"><circle cx="8" cy="8" r="6.8" fill="none" stroke="var(--blue)" stroke-width="1.5"/><path d="M4.8 8.2l2.2 2.2 4.2-4.6" fill="none" stroke="var(--blue)" stroke-width="1.6"/></svg>EV Charger Installation</li>
  </ul>

  <div class="abs contact">
    <h3 class="contact__title">CONTACT US</h3>
    <div class="contact__row"><svg width="12" height="12" viewBox="0 0 12 12"><rect x="3" y="0.5" width="6" height="11" rx="1.5" fill="#fff"/></svg>(415) 555-0142</div>
    <div class="contact__row"><svg width="12" height="12" viewBox="0 0 12 12"><rect x="0.5" y="2" width="11" height="8" rx="1" fill="none" stroke="#fff"/><path d="M1 2.5l5 4 5-4" fill="none" stroke="#fff"/></svg>service@halvorsenelectric.example</div>
    <div class="contact__row"><svg width="12" height="12" viewBox="0 0 12 12"><circle cx="6" cy="6" r="5.3" fill="none" stroke="#fff"/><ellipse cx="6" cy="6" rx="2.3" ry="5.3" fill="none" stroke="#fff"/><path d="M0.7 6h10.6" stroke="#fff"/></svg>www.halvorsenelectric.example</div>
    <div class="contact__row"><svg width="12" height="13" viewBox="0 0 12 13"><path d="M6 12.5C2.5 8 1.5 6.5 1.5 4.5a4.5 4.5 0 019 0c0 2-1 3.5-4.5 8z" fill="#fff"/><circle cx="6" cy="4.5" r="1.6" fill="var(--blue)"/></svg>120 Larkin Row, San Francisco,<br>CA 94103</div>
  </div>
</section>

<!-- Front page: intro and services -->
<section class="page page--front" aria-label="Flyer front page">
  <svg class="page__bg" width="540" height="764" viewBox="0 0 540 764" aria-hidden="true">
    <rect width="540" height="764" fill="var(--blue)"/>
    <circle cx="270" cy="0" r="250" fill="#fff"/>
    <path d="M0 440 C20 340 140 320 270 320 C400 320 520 340 540 440 L540 708 L0 708 Z" fill="var(--paper)"/>
    <rect y="734" width="540" height="3" fill="#fff"/>
    <rect y="744" width="540" height="2" fill="#fff"/>
  </svg>
  <div class="abs" role="img" aria-label="Photo of an electrician's gloved hand testing a breaker panel with a multimeter probe" style="left:28px;top:-242px;width:484px;height:484px;border-radius:50%;overflow:hidden;background:linear-gradient(160deg,#d8dadc 0%,#9aa2ab 50%,#5f6873 100%)">
    <div style="position:absolute;left:72px;top:-230px;width:340px;height:290px;border-radius:50%;background:var(--cyan);border:5px solid #fff"></div>
  </div>
  <div class="abs center front-brand">HALVORSEN ELECTRIC</div>

  <h1 class="abs center front-title">Halvorsen Electric</h1>
  <p class="abs front-intro">is a licensed electrical contractor proudly serving San Francisco and surrounding Bay Area communities. Our experienced electricians provide safe, efficient, and code-compliant electrical solutions for residential and commercial properties.</p>
  <div class="abs center front-tagline">ELECTRICAL / DATACOM</div>
  <div class="abs front-rule"></div>

  <h3 class="abs col-title" style="top:506px;left:28px">OUR SERVICES</h3>
  <ul class="abs services">
    <li><svg width="18" height="18" viewBox="0 0 18 18"><rect width="18" height="18" rx="3" fill="var(--ink)"/><path d="M4 9l5-4.5L14 9v5H4z" fill="#fff"/></svg>Residential Electrical</li>
    <li class="is-blue"><svg width="18" height="18" viewBox="0 0 18 18"><rect width="18" height="18" rx="3" fill="var(--blue)"/><path d="M10 3L5 10h3.5L7.5 15 13 8H9.5z" fill="#fff"/></svg>Electrical repairs &amp; troubleshooting</li>
    <li><svg width="18" height="18" viewBox="0 0 18 18"><rect width="18" height="18" rx="3" fill="var(--ink)"/><rect x="5" y="4" width="8" height="10" fill="none" stroke="#fff" stroke-width="1.4"/></svg>Panel upgrades &amp; breaker replacement</li>
    <li class="is-blue"><svg width="18" height="18" viewBox="0 0 18 18"><rect width="18" height="18" rx="3" fill="var(--blue)"/><circle cx="9" cy="9" r="3.5" fill="#fff"/></svg>Lighting installation (indoor &amp; outdoor)</li>
    <li><svg width="18" height="18" viewBox="0 0 18 18"><rect width="18" height="18" rx="3" fill="var(--ink)"/><rect x="6" y="4" width="6" height="10" rx="1" fill="#fff"/></svg>EV charger installation</li>
    <li class="is-blue"><svg width="18" height="18" viewBox="0 0 18 18"><rect width="18" height="18" rx="3" fill="var(--blue)"/><path d="M4 6h10M4 9h10M4 12h10" stroke="#fff" stroke-width="1.4"/></svg>Rewiring &amp; remodels</li>
    <li><svg width="18" height="18" viewBox="0 0 18 18"><rect width="18" height="18" rx="3" fill="var(--ink)"/><path d="M10 3L5 10h3.5L7.5 15 13 8H9.5z" fill="#fff"/></svg>Emergency electrical services</li>
  </ul>

  <h3 class="abs col-title" style="top:500px;left:290px">COMMERCIAL ELECTRICAL</h3>
  <ul class="abs commercial">
    <li><svg width="14" height="14" viewBox="0 0 16 16"><circle cx="8" cy="8" r="6.8" fill="none" stroke="var(--blue)" stroke-width="1.5"/><path d="M4.8 8.2l2.2 2.2 4.2-4.6" fill="none" stroke="var(--blue)" stroke-width="1.6"/></svg>Office &amp; retail electrical systems</li>
    <li><svg width="14" height="14" viewBox="0 0 16 16"><circle cx="8" cy="8" r="6.8" fill="none" stroke="var(--blue)" stroke-width="1.5"/><path d="M4.8 8.2l2.2 2.2 4.2-4.6" fill="none" stroke="var(--blue)" stroke-width="1.6"/></svg>Electrical inspections</li>
    <li><svg width="14" height="14" viewBox="0 0 16 16"><circle cx="8" cy="8" r="6.8" fill="none" stroke="var(--blue)" stroke-width="1.5"/><path d="M4.8 8.2l2.2 2.2 4.2-4.6" fill="none" stroke="var(--blue)" stroke-width="1.6"/></svg>Lighting upgrades &amp; maintenance</li>
    <li><svg width="14" height="14" viewBox="0 0 16 16"><circle cx="8" cy="8" r="6.8" fill="none" stroke="var(--blue)" stroke-width="1.5"/><path d="M4.8 8.2l2.2 2.2 4.2-4.6" fill="none" stroke="var(--blue)" stroke-width="1.6"/></svg>Tenant improvements</li>
    <li><svg width="14" height="14" viewBox="0 0 16 16"><circle cx="8" cy="8" r="6.8" fill="none" stroke="var(--blue)" stroke-width="1.5"/><path d="M4.8 8.2l2.2 2.2 4.2-4.6" fill="none" stroke="var(--blue)" stroke-width="1.6"/></svg>Emergency electrical services</li>
  </ul>
  <div class="abs photo-thumb" style="left:290px" role="img" aria-label="Photo of an electrician in a hard hat working at a control panel"></div>
  <div class="abs photo-thumb" style="left:410px;background:linear-gradient(135deg,#8a98a8,#d7dde3 50%,#e09a35)" role="img" aria-label="Photo of an electrician in a safety vest inspecting switchgear"></div>
</section>

</body>
</html>
```